Hollow Lantern Distillery

I need a label designed for my small distillery. I’d like it to have a rose, and the name hollow lantern in script writing. I need the graphic to fit a standard gin bottle and I’ll need to be able to edit it depending on alcohol, warning and descriptions. I want it to look elegant and attractive, but slightly daring too. It’s a 700ml oslo bottle
Target Market(s)
Bespoke gin and vodka drinkers
Industry/Entity Type
Beverage
Font styles to use
Script
Other font styles liked:
- Something easy to read
Requirements
Must have
- Room for me to add and remove text depending on the drink
Nice to have
- Hollow lantern in script, slight colour on the rose and black writing

```html
<!DOCTYPE html>
<html lang="en">
<head>
<meta charset="utf-8">
<title>Hollow Lantern Distillery – Gin Label</title>
<link rel="stylesheet" href="https://fonts.googleapis.com/css2?family=Bebas+Neue&family=Yesteryear&family=Playball&display=swap">
<style>
  :root {
    --page: #ffffff;
    --paper: #fcfaf5;
    --paper-edge: #e2e0dc;
    --teal: #8cc5d0;
    --teal-soft: #b6dbe2;
    --ink: #141414;
    --script: "Yesteryear", "Playball", cursive;
    --caps: "Bebas Neue", sans-serif;
  }
  * { box-sizing: border-box; margin: 0; padding: 0; }
  html, body {
    width: 1052px;
    height: 1200px;
    overflow: hidden;
    background: var(--page);
  }
  .label {
    position: absolute;
    left: 130px;
    top: 170px;
    width: 812px;
    height: 883px;
    background: var(--paper);
    border: 1px solid var(--paper-edge);
  }
  .label__frame {
    position: absolute;
    left: 20px;
    top: 14px;
    right: 15px;
    bottom: 17px;
    border: 3px solid var(--teal);
  }
  .brand {
    position: absolute;
    left: 0;
    right: 0;
    top: 40px;
    text-align: center;
    font-family: var(--script);
    font-weight: 400;
    color: var(--ink);
    line-height: 0.92;
  }
  .brand__line {
    display: block;
    font-size: 82px;
  }
  .brand__sub {
    display: block;
    font-size: 34px;
    margin-top: 2px;
    padding-left: 140px;
  }
  .rose {
    position: absolute;
    left: 297px;
    top: 256px;
    width: 211px;
    height: 514px;
    border-radius: 46% 46% 30% 30% / 22% 22% 10% 10%;
    background: linear-gradient(180deg, var(--teal-soft) 0%, var(--teal) 60%, var(--teal-soft) 100%);
    opacity: 0.85;
  }
  .product-name {
    position: absolute;
    left: 0;
    right: 0;
    top: 405px;
    text-align: center;
    font-family: var(--script);
    font-weight: 400;
    font-size: 300px;
    line-height: 1;
    color: var(--ink);
  }
  .details {
    position: absolute;
    left: 0;
    right: 0;
    top: 795px;
    font-family: var(--caps);
    font-size: 34px;
    color: var(--ink);
    letter-spacing: 2px;
  }
  .details__item { position: absolute; top: 0; white-space: nowrap; }
  .details__volume { left: 96px; }
  .details__estimated { letter-spacing: 0; }
  .details__origin { left: 264px; letter-spacing: 2.5px; }
  .details__strength { left: 622px; letter-spacing: 3px; }
</style>
</head>
<body>
  <main class="label">
    <div class="label__frame"></div>

    <h1 class="brand">
      <span class="brand__line">Hollow</span>
      <span class="brand__line">Lantern</span>
      <span class="brand__sub">Distillery</span>
    </h1>

    <div class="rose" role="img" aria-label="Engraved illustration of a single long-stemmed rose with leaves, printed in pale teal"></div>

    <p class="product-name">Gin</p>

    <div class="details">
      <span class="details__item details__volume">700 ML <span class="details__estimated">℮</span></span>
      <span class="details__item details__origin">PRODUCT OF AUSTRALIA</span>
      <span class="details__item details__strength">40%ABV</span>
    </div>
  </main>
</body>
</html>
```